Morvela Aesthetic Doctor

I require an elegant, luxurious looking business card for my aesthetic business. I am a doctor and that will set me aside from competitors. I am planning to provide home and spa based treatments to clients with high expectations. I have attached my logo.

```html
<!DOCTYPE html>
<html lang="en">
<head>
<meta charset="utf-8">
<title>Morvela Aesthetic Doctor – Business Card</title>
<link href="https://fonts.googleapis.com/css2?family=Open+Sans:wght@400;600&display=swap" rel="stylesheet">
<style>
  :root {
    --backdrop: #e6e6e6;
    --card: #f4f4f4;
    --ink: #222222;
    --mark-grey: #9a9a9c;
    --brand-blue: #1aa3e0;
    --stripe-1: #1c6db2;
    --stripe-2: #1a7dc1;
    --stripe-3: #2b8fd0;
    --stripe-4: #4fa7dc;
    --stripe-5: #79c3e7;
    --stripe-6: #a7d9ef;
  }
  * { box-sizing: border-box; margin: 0; padding: 0; }
  html, body { width: 1200px; height: 960px; overflow: hidden; }
  body {
    background: var(--backdrop);
    font-family: "Open Sans", sans-serif;
    position: relative;
  }
  .card {
    position: absolute;
    left: 320px;
    width: 560px;
    height: 340px;
    background: var(--card);
    overflow: hidden;
  }
  .card--front { top: 120px; }
  .card--back { top: 498px; }

  .stripe {
    position: absolute;
    left: 0; right: 0; bottom: 0;
    height: 16px;
    display: flex;
  }
  .stripe span { flex: 1; }
  .stripe span:nth-child(1), .stripe span:nth-child(11) { background: var(--stripe-1); }
  .stripe span:nth-child(2), .stripe span:nth-child(10) { background: var(--stripe-2); }
  .stripe span:nth-child(3), .stripe span:nth-child(9) { background: var(--stripe-3); }
  .stripe span:nth-child(4), .stripe span:nth-child(8) { background: var(--stripe-4); }
  .stripe span:nth-child(5), .stripe span:nth-child(7) { background: var(--stripe-5); }
  .stripe span:nth-child(6) { background: var(--stripe-6); }

  .brand {
    position: absolute;
    display: flex;
    align-items: center;
    gap: 22px;
  }
  .brand__dot {
    border: 3px solid var(--mark-grey);
    border-radius: 50%;
    flex: none;
  }
  .brand__name {
    color: var(--mark-grey);
    font-weight: 400;
    letter-spacing: 0.02em;
    white-space: nowrap;
  }
  .brand__line { display: block; }
  .card--front .brand { left: 70px; top: 88px; }
  .card--front .brand__dot { width: 110px; height: 110px; }
  .card--front .brand__name { font-size: 32px; line-height: 42px; }

  .services {
    position: absolute;
    left: 0; right: 0; top: 238px;
    text-align: center;
    font-size: 17px;
    line-height: 21px;
    color: var(--ink);
  }

  .card--back .brand { left: 82px; top: 30px; }
  .card--back .brand__dot { width: 112px; height: 112px; }

  .doctor { position: absolute; left: 38px; top: 168px; }
  .doctor__name { font-size: 20px; color: var(--ink); line-height: 26px; }
  .doctor__post { font-size: 12px; color: var(--brand-blue); margin-left: 4px; }
  .doctor__diploma { font-size: 14px; color: var(--brand-blue); line-height: 20px; }

  .divider {
    position: absolute;
    left: 38px; top: 227px;
    width: 485px; height: 1.5px;
    background: var(--brand-blue);
  }

  .contacts {
    position: absolute;
    left: 38px; top: 240px;
    list-style: none;
    font-size: 17px;
    line-height: 21.5px;
    color: var(--ink);
  }
  .contacts li { display: flex; align-items: center; gap: 5px; }
  .contacts svg { width: 13px; height: 13px; fill: none; stroke: var(--brand-blue); stroke-width: 1.6; }
  .contacts .icon-phone { fill: var(--brand-blue); stroke: none; }

  .social {
    position: absolute;
    right: 37px; top: 287px;
    display: flex; gap: 5px;
  }
  .social span {
    width: 13px; height: 13px;
    border-radius: 50%;
    background: var(--brand-blue);
  }
</style>
</head>
<body>

<section class="card card--front" aria-label="Card front">
  <div class="brand">
    <span class="brand__dot"></span>
    <span class="brand__name"><span class="brand__line">Morvela</span><span class="brand__line">Aesthetic Doctor</span></span>
  </div>
  <p class="services">
    Dermal injectables - Plasma facials - Microneedling<br>
    Skin boosters - Excessive sweating<br>
    Home and Spa Based Treatments
  </p>
  <div class="stripe"><span></span><span></span><span></span><span></span><span></span><span></span><span></span><span></span><span></span><span></span><span></span></div>
</section>

<section class="card card--back" aria-label="Card back">
  <div class="brand">
    <span class="brand__dot"></span>
  </div>
  <div class="doctor">
    <p class="doctor__name">Dr Elin Varga<span class="doctor__post">MRCPCH MD</span></p>
    <p class="doctor__diploma">Australasian Diploma of Aesthetic Medicine</p>
  </div>
  <div class="divider"></div>
  <ul class="contacts">
    <li>
      <svg class="icon-phone" viewBox="0 0 16 16" aria-hidden="true"><path d="M3.5 1.5l2.5 0 1 3.5-1.6 1.2a9 9 0 0 0 4.4 4.4L11 9l3.5 1v2.5c0 1-1 2-2 2C6.5 14.5 1.5 9.5 1.5 3.5c0-1 1-2 2-2z"/></svg>
      0800 555 014
    </li>
    <li>
      <svg viewBox="0 0 16 16" aria-hidden="true"><rect x="1.5" y="3.5" width="13" height="9"/><path d="M1.5 3.5l6.5 5 6.5-5"/></svg>
      elin@morvela.co.nz
    </li>
    <li>
      <svg viewBox="0 0 16 16" aria-hidden="true"><circle cx="8" cy="8" r="6.5"/><ellipse cx="8" cy="8" rx="2.8" ry="6.5"/><path d="M1.5 8h13"/></svg>
      www.morvela.co.nz
    </li>
  </ul>
  <div class="social" aria-label="Social channels"><span></span><span></span></div>
  <div class="stripe"><span></span><span></span><span></span><span></span><span></span><span></span><span></span><span></span><span></span><span></span><span></span></div>
</section>

</body>
</html>
```